Webdesign for blog, vlog and website
The designs for my website were better than what I expected when I started this contest. I knew I needed a call-to-action on my homepage, but I thought it wouldn't be possible and I didn't ask for it either. But Anselmo did it anyway. Furthermore, his design looked very good. For that reason I selected him as winner already before I should. I am very happy.

```html
<!DOCTYPE html>
<html lang="en">
<head>
<meta charset="utf-8">
<title>Veltoria – blog, vlog &amp; shop</title>
<link href="https://fonts.googleapis.com/css2?family=Lato:ital,wght@0,300;0,400;0,700;1,300;1,400&family=Merriweather:wght@300;400&display=swap" rel="stylesheet">
<style>
:root{
  --blue:#1a86d2;
  --blue-soft:#3b97d6;
  --ink:#222;
  --muted:#8a8a8a;
  --line:#e6e6e6;
  --band:#f7f7f7;
  --footer:#ececec;
}
*{box-sizing:border-box;margin:0;padding:0}
html,body{width:1200px;height:2518px;overflow:hidden;background:#fff}
body{position:relative;font-family:"Lato",sans-serif;color:var(--ink)}
.abs{position:absolute}
.serif{font-family:"Merriweather",serif;font-weight:300}
/* top bar */
.topbar{left:0;top:0;width:1200px;height:25px;border-bottom:1px solid var(--line)}
.topbar .cell{top:0;height:25px;border-left:1px solid var(--line);display:flex;align-items:center;justify-content:center;gap:6px;font-size:9px;color:#666}
/* header */
.logo{left:133px;top:38px;display:flex;align-items:center;gap:6px}
.logo .mark{width:22px;height:22px;border-radius:50%;background:var(--blue)}
.logo .name{font-size:20px;font-weight:700;color:var(--blue)}
.nav{top:57px;font-size:10px;font-weight:700;color:var(--blue);letter-spacing:.2px}
.search{left:880px;top:67px;width:170px;border-bottom:1px solid #ccc}
/* hero */
.photo{background:linear-gradient(160deg,#6d4f40 0%,#9a8c6e 30%,#c8cf52 45%,#7b7f85 65%,#b9bec4 100%)}
.hero{left:131px;top:97px;width:937px;height:488px}
.arrow{width:29px;height:29px;border:1px solid #d8d8d8;border-radius:50%;display:flex;align-items:center;justify-content:center}
.card{background:#fff;border:1px solid #f0f0f0;text-align:center}
.badge{width:26px;height:26px;border-radius:50%;background:#fff;display:flex;align-items:center;justify-content:center}
.badge i{width:18px;height:18px;border-radius:50%;background:var(--blue);display:flex;align-items:center;justify-content:center}
.date{font-size:8px;font-style:italic;font-weight:300;color:var(--muted)}
.btn{background:var(--blue);color:#fff;font-size:10px;display:flex;align-items:center;justify-content:center}
.btn-o{border:1px solid var(--blue);color:var(--blue);background:#fff;font-size:9.5px;display:flex;align-items:center;justify-content:center}
.post-title{font-size:14.5px;line-height:17px;color:#111}
.bee{background:linear-gradient(135deg,#55643c 0%,#8c6e2a 35%,#c99a2a 50%,#9c6ac8 75%,#b48ce0 100%)}
.plane{background:linear-gradient(180deg,#cfd5dc 0%,#e6e9ec 40%,#f4f5f6 55%,#8d9295 75%,#6d7378 100%)}
.section-title{font-family:"Merriweather",serif;font-weight:300;font-size:14px;color:#222}
.rule{height:1px;background:var(--line)}
.mini-title{font-family:"Merriweather",serif;font-size:10px;line-height:12.5px;color:#222}
.mini-link{font-size:8.5px;color:var(--blue)}
.shop-tile{width:137px;height:137px}
.shop-label{font-size:10.5px;color:var(--blue);text-align:center;width:160px}
.blue-panel{background:linear-gradient(135deg,#2e8fd6,#3a9de0 60%,#2b88cc)}
.foot-link{font-size:10.5px;color:#888;font-weight:300}
</style>
</head>
<body>

<!-- top bar -->
<div class="abs topbar"></div>
<div class="abs topbar" style="border:0;height:0"></div>
<div class="abs topbar cell" style="left:878px;width:42px;border-left:1px solid #e6e6e6">
  <svg width="9" height="9" viewBox="0 0 10 10"><circle cx="5" cy="3" r="2.3" fill="#1a86d2"/><path d="M1 10c0-3 8-3 8 0z" fill="#1a86d2"/></svg>
</div>
<div class="abs topbar cell" style="left:920px;width:77px">
  <svg width="11" height="9" viewBox="0 0 12 10"><path d="M0 1h2l2 6h6l2-5H3" fill="none" stroke="#1a86d2" stroke-width="1.4"/><circle cx="5" cy="9" r="1" fill="#1a86d2"/><circle cx="9" cy="9" r="1" fill="#1a86d2"/></svg>SHOP
</div>
<div class="abs topbar cell" style="left:997px;width:71px;border-right:1px solid #e6e6e6">
  <svg width="9" height="9" viewBox="0 0 10 10"><circle cx="5" cy="5" r="4.5" fill="#1a86d2"/></svg>EN ▾
</div>

<!-- header -->
<div class="abs logo"><span class="mark"></span><span class="name">Veltoria</span></div>
<div class="abs nav" style="left:373px">HOME</div>
<div class="abs nav" style="left:456px">BLOG</div>
<div class="abs nav" style="left:535px">VLOG</div>
<div class="abs nav" style="left:615px">FORUM</div>
<div class="abs nav" style="left:704px">OVER.ONS</div>
<div class="abs nav" style="left:807px">CONTACT</div>
<div class="abs search"></div>
<svg class="abs" style="left:1057px;top:58px" width="11" height="11" viewBox="0 0 12 12"><circle cx="5" cy="5" r="4" fill="none" stroke="#1a86d2" stroke-width="1.5"/><path d="M8 8l3.5 3.5" stroke="#1a86d2" stroke-width="1.5"/></svg>

<!-- hero -->
<div class="abs photo hero" role="img" aria-label="Runner in a yellow race shirt holding hands with a small girl in a pink helmet near the finish area"></div>
<div class="abs arrow" style="left:57px;top:327px"><svg width="8" height="10"><path d="M6 1L2 5l4 4" fill="none" stroke="#ccc"/></svg></div>
<div class="abs arrow" style="left:1114px;top:327px"><svg width="8" height="10"><path d="M2 1l4 4-4 4" fill="none" stroke="#ccc"/></svg></div>
<div class="abs card" style="left:288px;top:487px;width:620px;height:175px"></div>
<div class="abs badge" style="left:585px;top:474px;width:30px;height:30px"><i style="width:22px;height:22px"><svg width="9" height="11"><rect x="1" y="1" width="7" height="9" fill="none" stroke="#fff" stroke-width="1.3"/></svg></i></div>
<div class="abs date" style="left:288px;top:525px;width:620px;text-align:center;font-size:10px">Thursday 02, Nov 2017</div>
<div class="abs serif" style="left:288px;top:555px;width:620px;text-align:center;font-size:23px;line-height:30px;color:#111">Running has an enormous impact on our<br>bodies: how does this affect the heart</div>
<div class="abs btn" style="left:518px;top:645px;width:161px;height:32px;font-size:11px">READ POST</div>

<!-- post grid -->
<!-- row 1 -->
<div class="abs bee" role="img" aria-label="Bee on a purple flower" style="left:131px;top:745px;width:296px;height:199px"></div>
<div class="abs card" style="left:150px;top:910px;width:264px;height:120px"></div>
<div class="abs badge" style="left:266px;top:896px"><i><svg width="8" height="8"><path d="M2 1l5 3-5 3z" fill="#fff"/></svg></i></div>
<div class="abs date" style="left:150px;top:932px;width:264px;text-align:center">Thursday 02, Nov 2017</div>
<div class="abs serif post-title" style="left:150px;top:950px;width:264px;text-align:center">The annihilation of flying insects in Germany is an extremely worrying sign</div>
<div class="abs btn" style="left:210px;top:1015px;width:142px;height:30px">READ POST</div>

<div class="abs plane" role="img" aria-label="White private jet parked on an airfield" style="left:453px;top:745px;width:296px;height:199px"></div>
<div class="abs card" style="left:472px;top:910px;width:264px;height:120px"></div>
<div class="abs badge" style="left:588px;top:896px"><i><svg width="8" height="10"><rect x="1" y="1" width="6" height="8" fill="none" stroke="#fff" stroke-width="1.2"/></svg></i></div>
<div class="abs date" style="left:472px;top:932px;width:264px;text-align:center">Wednesday 18, Oct 2017</div>
<div class="abs serif post-title" style="left:472px;top:950px;width:264px;text-align:center">The annihilation of flying insects in Germany is an extremely worrying sign</div>
<div class="abs btn" style="left:532px;top:1015px;width:142px;height:30px">READ POST</div>

<!-- row 2 -->
<div class="abs bee" role="img" aria-label="Bee on a purple flower" style="left:131px;top:1104px;width:296px;height:199px"></div>
<div class="abs card" style="left:150px;top:1269px;width:264px;height:120px"></div>
<div class="abs badge" style="left:266px;top:1255px"><i><svg width="8" height="8"><path d="M2 1l5 3-5 3z" fill="#fff"/></svg></i></div>
<div class="abs date" style="left:150px;top:1291px;width:264px;text-align:center">Thursday 02, Nov 2017</div>
<div class="abs serif post-title" style="left:150px;top:1309px;width:264px;text-align:center">The annihilation of flying insects in Germany is an extremely worrying sign</div>
<div class="abs btn" style="left:210px;top:1374px;width:142px;height:30px">READ POST</div>

<div class="abs plane" role="img" aria-label="White private jet parked on an airfield" style="left:453px;top:1104px;width:296px;height:199px"></div>
<div class="abs card" style="left:472px;top:1269px;width:264px;height:120px"></div>
<div class="abs badge" style="left:588px;top:1255px"><i><svg width="8" height="10"><rect x="1" y="1" width="6" height="8" fill="none" stroke="#fff" stroke-width="1.2"/></svg></i></div>
<div class="abs date" style="left:472px;top:1291px;width:264px;text-align:center">Wednesday 18, Oct 2017</div>
<div class="abs serif post-title" style="left:472px;top:1309px;width:264px;text-align:center">The annihilation of flying insects in Germany is an extremely worrying sign</div>
<div class="abs btn" style="left:532px;top:1374px;width:142px;height:30px">READ POST</div>

<!-- row 3 -->
<div class="abs bee" role="img" aria-label="Bee on a purple flower" style="left:131px;top:1462px;width:296px;height:199px"></div>
<div class="abs card" style="left:150px;top:1627px;width:264px;height:120px"></div>
<div class="abs badge" style="left:266px;top:1613px"><i><svg width="8" height="8"><path d="M2 1l5 3-5 3z" fill="#fff"/></svg></i></div>
<div class="abs date" style="left:150px;top:1649px;width:264px;text-align:center">Thursday 02, Nov 2017</div>
<div class="abs serif post-title" style="left:150px;top:1667px;width:264px;text-align:center">The annihilation of flying insects in Germany is an extremely worrying sign</div>
<div class="abs btn" style="left:210px;top:1732px;width:142px;height:30px">READ POST</div>

<div class="abs plane" role="img" aria-label="White private jet parked on an airfield" style="left:453px;top:1462px;width:296px;height:199px"></div>
<div class="abs card" style="left:472px;top:1627px;width:264px;height:120px"></div>
<div class="abs badge" style="left:588px;top:1613px"><i><svg width="8" height="10"><rect x="1" y="1" width="6" height="8" fill="none" stroke="#fff" stroke-width="1.2"/></svg></i></div>
<div class="abs date" style="left:472px;top:1649px;width:264px;text-align:center">Wednesday 18, Oct 2017</div>
<div class="abs serif post-title" style="left:472px;top:1667px;width:264px;text-align:center">The annihilation of flying insects in Germany is an extremely worrying sign</div>
<div class="abs btn" style="left:532px;top:1732px;width:142px;height:30px">READ POST</div>

<!-- all posts -->
<div class="abs" style="left:399px;top:1817px;font-size:11px;color:var(--blue);display:flex;gap:9px;align-items:center">ALL POSTS
  <svg width="10" height="9"><path d="M1 1l3.5 3.5L1 8M5 1l3.5 3.5L5 8" fill="none" stroke="#1a86d2" stroke-width="1.5"/></svg></div>

<!-- sidebar: about -->
<div class="abs section-title" style="left:772px;top:743px">ABOUT ME</div>
<div class="abs rule" style="left:862px;top:752px;width:210px"></div>
<div class="abs" role="img" aria-label="Portrait of the blogger, a smiling woman with long hair in a light blue t-shirt" style="left:845px;top:782px;width:162px;height:186px;background:linear-gradient(180deg,#f7f7f7 0%,#e9d5c4 40%,#8cc8e8 75%,#8cc8e8 100%);border-radius:2px"></div>
<div class="abs card" style="left:789px;top:968px;width:264px;height:86px"></div>
<div class="abs" style="left:800px;top:990px;width:242px;text-align:center;font-size:10.5px;line-height:15px;color:#777">I'm glad that you want to contact me. I welcome it, whether it is a question, idea or a complaint.</div>
<div class="abs btn-o" style="left:848px;top:1038px;width:143px;height:30px">MORE INFO</div>

<!-- most read -->
<div class="abs section-title" style="left:772px;top:1106px">MOST READ POSTS:</div>
<div class="abs rule" style="left:922px;top:1114px;width:148px"></div>

<div class="abs" role="img" aria-label="City towers with smoke and fire" style="left:771px;top:1144px;width:137px;height:88px;background:linear-gradient(135deg,#7f8a95,#b2b7bc 45%,#e07a2c 70%,#6d6f72)"></div>
<div class="abs date" style="left:918px;top:1151px;font-size:7px">Wednesday 18, Oct 2017</div>
<div class="abs mini-title" style="left:918px;top:1170px;width:150px">9/11 has changed everything</div>
<div class="abs mini-link" style="left:918px;top:1218px">READ MORE</div>

<div class="abs" role="img" aria-label="Video still of a speaker with a title card about democracy" style="left:771px;top:1253px;width:137px;height:88px;background:linear-gradient(90deg,#2b6fb6 0%,#3a86cc 45%,#e3e7ee 75%,#c7ccd4 100%)"></div>
<div class="abs date" style="left:918px;top:1260px;font-size:7px">Wednesday 18, Oct 2017</div>
<div class="abs mini-title" style="left:918px;top:1279px;width:155px">Why is it so hard to establish democracy in other cultures?</div>
<div class="abs mini-link" style="left:918px;top:1327px">READ MORE</div>

<div class="abs" role="img" aria-label="Busy airport departure hall with travellers" style="left:771px;top:1362px;width:137px;height:88px;background:linear-gradient(180deg,#5a6a8a,#a3a8b3 50%,#7b7f88)"></div>
<div class="abs date" style="left:918px;top:1369px;font-size:7px">Wednesday 18, Oct 2017</div>
<div class="abs mini-title" style="left:918px;top:1388px;width:155px">If you booked a flight you might have rights if your flight is delayed or cancelled</div>
<div class="abs mini-link" style="left:918px;top:1436px">READ MORE</div>

<!-- newsletter -->
<div class="abs blue-panel" role="img" aria-label="Blue-tinted desk scene with a plant and notebook" style="left:773px;top:1488px;width:296px;height:184px"></div>
<div class="abs serif" style="left:773px;top:1523px;width:296px;text-align:center;color:#fff;font-size:13.5px">NEWSLETTER VELTORIA</div>
<div class="abs" style="left:850px;top:1563px;width:142px;height:29px;background:#fff;font-size:8.5px;color:#bbb;font-style:italic;display:flex;align-items:center;justify-content:center">E-mail</div>
<div class="abs btn" style="left:850px;top:1604px;width:142px;height:29px;font-size:9.5px">SUBSCRIBE</div>

<!-- shop now -->
<div class="abs rule" style="left:129px;top:1881px;width:943px;background:#dde6ee"></div>
<div class="abs section-title" style="left:543px;top:1870px;width:111px;height:24px;background:#fff;text-align:center;line-height:22px">SHOP NOW</div>

<div class="abs shop-tile" role="img" aria-label="Painted pebbles with words" style="left:131px;top:1929px;background:linear-gradient(135deg,#a89a86,#d6c6ae 50%,#8a7a6a)"></div>
<div class="abs shop-tile" role="img" aria-label="Framed hot air balloon prints" style="left:291px;top:1929px;background:linear-gradient(180deg,#f2f2f2,#e6e6e6)"></div>
<div class="abs shop-tile" role="img" aria-label="Silver bar necklace" style="left:451px;top:1929px;background:linear-gradient(135deg,#2c3c55,#c4a48a 50%,#d8b9a0)"></div>
<div class="abs shop-tile" role="img" aria-label="Yellow and navy beach volleyball" style="left:612px;top:1929px;background:radial-gradient(circle,#e2e61a 0%,#d0d71c 45%,#1b2a5e 70%,#fff 71%)"></div>
<div class="abs shop-tile" role="img" aria-label="Rustic metal welcome sign" style="left:772px;top:1929px;background:linear-gradient(180deg,#fff,#f0e8e4 50%,#fff)"></div>
<div class="abs shop-tile" role="img" aria-label="Engraved bar key chains with tassels" style="left:932px;top:1929px;background:linear-gradient(180deg,#f4efea,#e9ddd2)"></div>

<div class="abs shop-label" style="left:120px;top:2089px">WISHING STONES</div>
<div class="abs shop-label" style="left:280px;top:2089px">BANNERS</div>
<div class="abs shop-label" style="left:440px;top:2089px">JEWELLERY</div>
<div class="abs shop-label" style="left:601px;top:2089px">SPORTS&amp;GAMES</div>
<div class="abs shop-label" style="left:761px;top:2089px">FOR AT HOME</div>
<div class="abs shop-label" style="left:921px;top:2089px">KEY CHAINS</div>

<div class="abs rule" style="left:129px;top:2140px;width:943px;background:#dde6ee"></div>

<!-- bottom band -->
<div class="abs" style="left:0;top:2330px;width:1200px;height:135px;background:var(--band)"></div>
<div class="abs" style="left:0;top:2465px;width:1200px;height:53px;background:var(--footer)"></div>

<!-- recent posts -->
<div class="abs section-title" style="left:130px;top:2177px">RECENT POSTS:</div>
<div class="abs" role="img" aria-label="City towers with smoke and fire" style="left:132px;top:2215px;width:137px;height:88px;background:linear-gradient(135deg,#7f8a95,#b2b7bc 45%,#e07a2c 70%,#6d6f72)"></div>
<div class="abs date" style="left:280px;top:2222px;font-size:7px">Wednesday 18, Oct 2017</div>
<div class="abs mini-title" style="left:280px;top:2241px;width:150px">9/11 has changed everything</div>
<div class="abs mini-link" style="left:280px;top:2289px">READ MORE</div>

<div class="abs" role="img" aria-label="Busy airport departure hall with travellers" style="left:132px;top:2320px;width:137px;height:88px;background:linear-gradient(180deg,#5a6a8a,#a3a8b3 50%,#7b7f88)"></div>
<div class="abs date" style="left:280px;top:2327px;font-size:7px">Wednesday 18, Oct 2017</div>
<div class="abs mini-title" style="left:280px;top:2346px;width:150px">If you booked a flight you might have rights if your flight is delayed or cancelled</div>
<div class="abs mini-link" style="left:280px;top:2394px">READ MORE</div>

<!-- recent video -->
<div class="abs section-title" style="left:451px;top:2177px">RECENT VIDEO:</div>
<div class="abs" role="img" aria-label="Video still of a speaker with a title card about democracy" style="left:453px;top:2215px;width:137px;height:88px;background:linear-gradient(90deg,#2b6fb6 0%,#3a86cc 45%,#e3e7ee 75%,#c7ccd4 100%)"></div>
<div class="abs date" style="left:601px;top:2222px;font-size:7px">Wednesday 18, Oct 2017</div>
<div class="abs mini-title" style="left:601px;top:2241px;width:155px">Why is it so hard to establish democracy in other cultures?</div>
<div class="abs mini-link" style="left:601px;top:2289px">READ MORE</div>

<div class="abs" role="img" aria-label="Video still of a speaker with a title card about democracy" style="left:453px;top:2320px;width:137px;height:88px;background:linear-gradient(90deg,#2b6fb6 0%,#3a86cc 45%,#e3e7ee 75%,#c7ccd4 100%)"></div>
<div class="abs date" style="left:601px;top:2327px;font-size:7px">Wednesday 18, Oct 2017</div>
<div class="abs mini-title" style="left:601px;top:2346px;width:155px">Why is it so hard to establish democracy in other cultures?</div>
<div class="abs mini-link" style="left:601px;top:2394px">READ MORE</div>

<!-- contact -->
<div class="abs section-title" style="left:772px;top:2177px">CONTACT</div>
<div class="abs blue-panel" role="img" aria-label="Blue-tinted handwritten letter" style="left:773px;top:2215px;width:296px;height:155px"></div>
<div class="abs card" style="left:789px;top:2272px;width:262px;height:122px;text-align:left"></div>
<div class="abs serif" style="left:805px;top:2290px;width:232px;font-size:10px;line-height:12.5px;color:#222;text-align:justify">I'm glad that you want to contact me. I welcome it, whether it is a question, idea or a complaint.</div>
<div class="abs" style="left:805px;top:2332px;width:232px;font-size:10.5px;line-height:15px;color:#777">Fill out one of the forms below and I'll answer you as quickly as possible.</div>
<div class="abs btn-o" style="left:848px;top:2379px;width:143px;height:30px">MORE INFO</div>

<!-- footer -->
<div class="abs foot-link" style="left:457px;top:2485px">User agreement</div>
<div class="abs foot-link" style="left:564px;top:2485px">Privacy policy</div>
<div class="abs foot-link" style="left:663px;top:2485px">Terms of Service</div>

</body>
</html>
```